Verpackungen für Griffwärmer
Zielgruppe
Wir sind ein innovatives Start-Up und suchen ein hochwertiges Design für unser Produkt (Griffwärmer).
Unsere Zielgruppe sind größtenteils Mütter mit Kinderwagen.
Wir suchen Designer, die gerne etwas neues ausprobieren und sich auch an Herausforderungen trauen.
Aufgabenstellung
Das Design sollte vor allem Mütter mit Kleinkindern ansprechen. Die Verpackung ist eine Box (13,3cmX10cmX4,5cm)
Stanzkonturen sind beigefügt.
Ebenso das Bild, das im Mittelgrund stehen sollte.
Die Farbe soll eher emotional neutral gehalten sein (weiß beige) und hochwertig aussehen.
Auch ein modernes, professionelles Design ist gern gesehen.
Selbstverständlich kein langweiliges Design.
Auf der Rückseite soll die Gebrauchsanweisung zu finden sein.
Auf einer langen seitlichen Seite bitte 5.jpg einfügen. Dort soll daneben noch ein kurzer Text: 'Kinderleichtes Anbringen durch Klettverschluss'(oberes Bild) und
'schnelle Reaktivierung durch einfaches aufkochen'(unteres Bild)
Auf der Hauptseite Vorne bitte folgende Icons anbringen:
für Kinderwagen, Fahrrad, Roller und Flaschen/Gläser.
Ebenfalls wichtig ist '2 Stück' sowie der Name 'PalmGLOW™' und 'Griffwärmer'.
Als gezeichnete Pfeile zum Produkt hin noch 'universelle Größe' und 'mit Klettverschluss'. Die es als dazugemalte Pfeile zum Produkt hin noch zusätzlich beschreiben, als Handschrift sozusagen.
Die Schriftart bitte leicht feminin. Also nicht zu eckig.
Generell soll die Verpackung übersichtlich und nicht überladen wirken.
Anbei finden Sie die Gebrauchsanweisung und den PalmGLOW™ an sich.
Ebenfalls die aktuellen Stanzkonturen. Diese bitte zwingend beachten.
Das 5.jpg ist das beschreibende Bild für die Seite.
Das Design kann sowohl liegend, als auch stehend sein. Unsere Tendenz geht zum Liegenden, wir lassen uns jedoch auch gerne vom Gegenteil überzeugen.

```html
<!DOCTYPE html>
<html lang="de">
<head>
<meta charset="utf-8">
<title>PalmGLOW Griffwärmer – Faltschachtel</title>
<link href="https://fonts.googleapis.com/css2?family=Lato:ital,wght@0,300;0,400;0,700;0,900;1,400&family=Amatic+SC:wght@700&display=swap" rel="stylesheet">
<style>
  :root {
    --cream: #fbefdc;
    --sun: #f8d993;
    --sun-soft: #f9e3b0;
    --ink: #2b2b2b;
    --orange: #ee8140;
    --white: #ffffff;
    --photo-dark: #3a3836;
    --photo-light: #d9d4cc;
  }
  * { box-sizing: border-box; margin: 0; padding: 0; }
  html, body { width: 1200px; height: 1021px; overflow: hidden; background: var(--white); }
  body { font-family: "Lato", sans-serif; color: var(--ink); }

  .dieline {
    position: absolute; left: 0; top: 0;
    width: 2100px; height: 1787px;
    transform: scale(0.5714); transform-origin: 0 0;
  }
  .dieline-shapes, .front-arrows { position: absolute; left: 0; top: 0; }

  .abs { position: absolute; }

  /* photo placeholders */
  .photo { position: absolute; border: 3px solid var(--white); }
  .photo-attach { left: 200px; top: 485px; width: 236px; height: 152px;
    background: linear-gradient(135deg, var(--photo-dark) 0%, #6b6660 45%, #e4d6c4 100%); }
  .photo-boil { left: 200px; top: 740px; width: 236px; height: 153px;
    background: linear-gradient(160deg, #59684a 0%, #9a968d 40%, #3b3b3e 80%, #b0413b 100%); }
  .photo-product { left: 1067px; top: 880px; width: 470px; height: 392px;
    background: linear-gradient(200deg, #ece7df 0%, #cfc9c0 30%, #4a4846 58%, #262626 100%); }

  /* back panel copy */
  .copy { font-size: 16px; line-height: 20.6px; }
  .copy b { font-weight: 700; }
  .copy-usage { left: 447px; top: 485px; width: 330px; }
  .copy-usage-cont { left: 200px; top: 645px; width: 570px; }
  .copy-reactivate { left: 443px; top: 786px; width: 320px; }
  .copy-reactivate-cont { left: 200px; top: 902px; width: 570px; }
  .note { text-decoration: underline; font-style: italic; }

  .fine { font-size: 11.5px; line-height: 15.4px; font-weight: 300; }
  .fine h3 { font-size: 12.5px; font-weight: 700; margin-bottom: 4px; }
  .fine ul { padding-left: 17px; }
  .fine li { margin-bottom: 3px; }
  .fine-safety { left: 208px; top: 1000px; width: 275px; }
  .fine-burn { left: 508px; top: 1000px; width: 268px; }
  .ingredients { left: 208px; top: 1238px; font-size: 15px; }
  .ingredients b { font-weight: 700; }

  /* brand marks */
  .brand-name { font-family: "Lato", sans-serif; font-weight: 900; color: var(--ink); white-space: nowrap; line-height: 1; }
  .brand-sub { font-family: "Lato", sans-serif; font-weight: 300; color: var(--ink); white-space: nowrap; line-height: 1; }

  .lid-brand { left: 290px; top: 285px; width: 400px; text-align: center; transform: rotate(180deg); }
  .lid-brand .brand-name { font-size: 54px; }
  .lid-brand .brand-sub { font-size: 18px; letter-spacing: 8px; margin-top: 10px; }

  .side-brand { width: 560px; transform: rotate(-90deg); transform-origin: center; text-align: left; }
  .side-brand .brand-name { font-size: 90px; }
  .side-brand .brand-sub { font-size: 31px; letter-spacing: 15.5px; margin-top: 12px; padding-left: 175px; }
  .side-left { left: 650px; top: 810px; }
  .side-right { left: 1520px; top: 810px; }

  .claim-band { left: 1067px; top: 470px; width: 603px; height: 40px; background: var(--orange);
    color: var(--white); font-size: 21px; letter-spacing: 1.4px; text-align: center; line-height: 42px; }

  .front-brand { left: 1095px; top: 565px; width: 540px; text-align: right; }
  .front-brand .brand-name { font-size: 88px; }
  .front-brand .brand-sub { font-size: 31px; letter-spacing: 16px; margin-top: 14px; margin-right: -12px; }

  .hand-label { font-family: "Amatic SC", sans-serif; font-weight: 700; font-size: 25px; color: var(--ink); white-space: nowrap; }
  .label-velcro { left: 1090px; top: 792px; }
  .label-size { left: 1215px; top: 1026px; color: var(--white); }

  .pack-count { left: 1088px; top: 1180px; color: var(--white); display: flex; align-items: flex-end; }
  .pack-count .num { font-size: 74px; font-weight: 300; line-height: 1; }
  .pack-count .unit { font-size: 17px; writing-mode: vertical-rl; transform: rotate(180deg); margin-left: 2px; margin-bottom: 6px; }

  .use-icons { left: 1545px; top: 778px; }
</style>
</head>
<body>
<div class="dieline">
  <svg class="dieline-shapes" width="2100" height="1787" viewBox="0 0 2100 1787" aria-hidden="true">
    <defs>
      <linearGradient id="wash" x1="0" y1="0" x2="0" y2="1">
        <stop offset="0" stop-color="var(--cream)"/>
        <stop offset="0.25" stop-color="var(--sun-soft)"/>
        <stop offset="0.55" stop-color="var(--sun)"/>
        <stop offset="0.85" stop-color="var(--sun-soft)"/>
        <stop offset="1" stop-color="var(--cream)"/>
      </linearGradient>
    </defs>
    <g fill="var(--cream)">
      <path class="lid-flap" d="M190 470 V205 Q190 105 290 105 H700 Q795 105 795 205 V470 Z"/>
      <path class="glue-flap" d="M190 470 L123 488 V1255 L190 1272 Z"/>
      <path class="dust-flap" d="M795 470 V465 L818 445 V288 H1010 L1045 420 L1067 440 V470 Z"/>
      <path class="dust-flap" d="M797 1272 V1300 L818 1320 L850 1455 H1043 L1050 1292 L1067 1272 Z"/>
      <path class="base-flap" d="M1067 1272 V1545 Q1067 1640 1160 1640 H1578 Q1670 1640 1670 1545 V1272 Z"/>
      <path class="dust-flap" d="M1670 470 V440 L1690 420 L1720 288 H1915 V440 L1940 465 V470 Z"/>
      <path class="dust-flap" d="M1670 1272 L1688 1292 L1698 1455 H1888 L1920 1320 L1940 1300 V1272 Z"/>
    </g>
    <rect class="body-band" x="190" y="470" width="1750" height="802" fill="url(#wash)"/>
  </svg>

  <!-- lid -->
  <div class="abs lid-brand">
    <div class="brand-name">PalmGLOW™</div>
    <div class="brand-sub">GRIFFWÄRMER</div>
  </div>

  <!-- back panel -->
  <div class="photo photo-attach" role="img" aria-label="Foto: Hände bringen den Griffwärmer mit Klettverschluss am Kinderwagengriff an"></div>
  <div class="abs copy copy-usage">
    <b>Anwendung:</b><br>
    <b>1.</b> Vor der Anwendung bitte die Sicherheitshinweise lesen und beachten.<br>
    <b>2.</b> Drücken Sie das Metallplättchen im Inneren des PalmGLOW vorsichtig bis es „klickt“ und warten Sie, bis die Flüssigkeit vollständig kristallisiert ist. <span class="note">(Das Plättchen nicht biegen!)</span>
  </div>
  <div class="abs copy copy-usage-cont">
    <b>3.</b> Bringen Sie den PalmGLOW am gewünschten Griff mit dem Klettverschluss nach unten an. Dabei darf keine Funktion Ihres Geräts beeinträchtigt sein.<br>
    <b>4.</b> Genießen Sie je nach Außentemperatur bis zu 30 Minuten eine angenehme Wärme von bis zu 55 °C.
  </div>

  <div class="photo photo-boil" role="img" aria-label="Foto: Griffwärmer wird in einem Kochtopf auf dem Herd erhitzt"></div>
  <div class="abs copy copy-reactivate">
    <b>Reaktivierung:</b><br>
    1. Legen Sie den PalmGLOW nach dem Gebrauch für ca. 5-10 min in heißes Wasser, bis die Flüssigkeit im Inneren wieder vollständig klar ist.
  </div>
  <div class="abs copy copy-reactivate-cont">
    2. Nehmen Sie ihn anschließend vorsichtig heraus und lassen ihn abkühlen. Sie können den PalmGLOW jetzt erneut aktivieren.<br>
    Hinweis: Falls sich der PalmGLOW selbstständig auslösen sollte, ist das kein Defekt. Gehen Sie vor wie unter Reaktivierung beschrieben.
  </div>

  <div class="abs fine fine-safety">
    <h3>Sicherheitshinweise:</h3>
    <ul>
      <li>Bitte bringen Sie Ihren PalmGLOW nur an solchen Stellen an, die die Sicherheit Ihres Geräts nicht beeinträchtigen.</li>
      <li>PalmGLOW nicht mit scharfen oder spitzen Gegenständen verletzen.</li>
      <li>PalmGLOW nicht in der Mikrowelle erwärmen.</li>
      <li>Beschädigte PalmGLOW nicht weiterverwenden und ordnungsgemäß entsorgen.</li>
      <li>Kontakt mit Salzlösung vermeiden. Bei Hautkontakt gründlich reinigen.</li>
    </ul>
  </div>
  <div class="abs fine fine-burn">
    <h3>Verbrennungsgefahr!</h3>
    <ul>
      <li>Der PalmGLOW wird beim Kochen heiß, warten Sie nach dem Herausnehmen aus dem Wasser so lange, bis die ausgehende Wärme angenehm ist.</li>
      <li>Besonders nach dem Kochen ist der PalmGLOW sehr empfindlich gegenüber Druck und spitzen Gegenständen. Seien Sie gerade dann besonders vorsichtig.</li>
      <li>Dies ist kein Spielzeug, für Kinder unerreichbar aufbewahren.</li>
      <li>Den PalmGLOW nicht direkt nach dem Kochen auslösen.</li>
      <li>Den PalmGLOW nach dem Kochen nicht künstlich kühlen.</li>
    </ul>
  </div>
  <div class="abs ingredients"><b>Inhaltsstoffe:</b> Salzlösung, Metallplättchen, Wasser</div>

  <!-- side panels -->
  <div class="abs side-brand side-left">
    <div class="brand-name">PalmGLOW™</div>
    <div class="brand-sub">GRIFFWÄRMER</div>
  </div>
  <div class="abs side-brand side-right">
    <div class="brand-name">PalmGLOW™</div>
    <div class="brand-sub">GRIFFWÄRMER</div>
  </div>

  <!-- front panel -->
  <div class="abs claim-band">AN KALTEN WINTERTAGEN FÜR GRIFFE ALLER ART</div>
  <div class="abs front-brand">
    <div class="brand-name">PalmGLOW™</div>
    <div class="brand-sub">GRIFFWÄRMER</div>
  </div>

  <div class="photo-product abs" role="img" aria-label="Produktfoto: zwei transparente Griffwärmer an einem schwarzen Kinderwagengriff"></div>

  <svg class="front-arrows" width="2100" height="1787" viewBox="0 0 2100 1787" aria-hidden="true">
    <g fill="none" stroke="var(--ink)" stroke-width="2.5" stroke-linecap="round">
      <path d="M1135 828 Q1150 845 1156 868"/>
      <path d="M1146 858 L1156 870 L1159 853"/>
    </g>
    <g fill="none" stroke="var(--white)" stroke-width="2.5" stroke-linecap="round">
      <path d="M1355 1040 Q1385 1035 1400 1012"/>
      <path d="M1386 1014 L1401 1010 L1400 1026"/>
    </g>
  </svg>

  <div class="abs hand-label label-velcro">MIT KLETTVERSCHLUSS</div>
  <div class="abs hand-label label-size">UNIVERSELLE GRÖSSE</div>

  <div class="abs pack-count"><span class="num">2</span><span class="unit">STÜCK</span></div>

  <svg class="abs use-icons" width="100" height="460" viewBox="0 0 100 460" role="img" aria-label="Geeignet für Kinderwagen, Fahrrad, Roller und Flaschen oder Gläser">
    <g fill="var(--white)" stroke="var(--ink)" stroke-width="2">
      <circle cx="49" cy="48" r="48"/>
      <circle cx="49" cy="168" r="48"/>
      <circle cx="49" cy="288" r="48"/>
      <circle cx="49" cy="408" r="48"/>
    </g>
    <g fill="none" stroke="var(--ink)" stroke-width="2.6" stroke-linecap="round" stroke-linejoin="round">
      <path d="M32 42 H68 Q68 58 50 58 Q32 58 32 42 Z"/>
      <path d="M40 42 Q42 28 56 26 L60 42"/>
      <path d="M68 42 L74 30 H79"/>
      <path d="M38 58 L60 70 M60 58 L38 70"/>
      <circle cx="36" cy="72" r="4"/><circle cx="62" cy="72" r="4"/>
      <circle cx="32" cy="176" r="10"/><circle cx="66" cy="176" r="10"/>
      <path d="M32 176 L42 160 H62 L66 176 M42 160 L50 176 L62 160 M50 176 H32 M40 154 H46 M60 152 H66 L62 160"/>
      <circle cx="28" cy="304" r="5"/><circle cx="70" cy="304" r="5"/>
      <path d="M28 299 H62 L66 266 M60 266 H72 M33 304 H65"/>
      <path d="M26 396 L29 424 H43 L46 396 Z M27 404 H45"/>
      <path d="M58 424 V398 Q58 392 62 388 V378 H68 V388 Q72 392 72 398 V424 Z"/>
    </g>
  </svg>
</div>
</body>
</html>
```